K&T Holdings

Design a modern simple business card. I have attached a clean version of a card we like form Marrowfield Partners another company we own. I also attached the old K&T card design and logo and a couple of ideas we had but just can't finalize on whether we like them or not. We would like to include the 20 year logo somewhere on the card.

```html
<!DOCTYPE html>
<html lang="en">
<head>
<meta charset="utf-8">
<title>K&amp;T Holdings — Business Card</title>
<link href="https://fonts.googleapis.com/css2?family=Montserrat:wght@400;600;700&display=swap" rel="stylesheet">
<style>
  :root {
    --navy: #1d1d4f;
    --slate: #5e6063;
    --paper: #fbfbfa;
    --backdrop: #c9cccd;
  }
  * { box-sizing: border-box; margin: 0; padding: 0; }
  html, body { width: 1200px; height: 829px; overflow: hidden; }
  body {
    background: var(--backdrop);
    font-family: "Montserrat", Arial, sans-serif;
    position: relative;
  }
  .card {
    position: absolute;
    top: 266px;
    width: 520px;
    height: 297px;
    background: var(--paper);
    border-bottom: 4px solid var(--navy);
    box-shadow: 0 10px 24px rgba(0,0,0,.18);
    overflow: hidden;
  }
  .card--front { left: 50px; }
  .card--back { left: 630px; }

  /* Front */
  .name-bar {
    position: absolute; left: 0; top: 34px;
    width: 22px; height: 30px; background: var(--navy);
  }
  .identity { position: absolute; left: 40px; top: 32px; }
  .identity__name {
    font-weight: 700; font-size: 22px; color: var(--navy); letter-spacing: .5px;
  }
  .identity__title { font-size: 12px; color: var(--slate); margin-top: 2px; }
  .address { position: absolute; left: 40px; top: 100px; font-size: 12px; color: var(--slate); line-height: 1.35; }
  .address__label { font-weight: 700; color: var(--navy); }
  .contacts { position: absolute; left: 40px; top: 168px; list-style: none; font-size: 12px; color: var(--slate); }
  .contacts li { display: flex; align-items: center; gap: 8px; height: 19px; }
  .contacts svg { width: 11px; height: 11px; fill: var(--navy); flex: none; }

  .brand { position: absolute; display: flex; align-items: center; gap: 10px; }
  .brand__dot { width: 18px; height: 18px; border-radius: 50%; background: var(--navy); }
  .brand__name { font-weight: 700; color: var(--navy); }
  .card--front .brand { right: 44px; bottom: 40px; }
  .card--front .brand__name { font-size: 46px; }

  /* Back */
  .card--back .brand { left: 70px; top: 92px; }
  .card--back .brand__name { font-size: 48px; }
  .divider { position: absolute; left: 272px; top: 62px; width: 1px; height: 110px; background: var(--navy); }
  .anniversary { position: absolute; left: 296px; top: 80px; color: var(--navy); font-weight: 700; line-height: 1.1; }
  .anniversary__years { font-size: 34px; }
  .anniversary__span { font-size: 20px; }
  .tagline { position: absolute; left: 0; right: 0; top: 200px; text-align: center; }
  .tagline__lead { font-weight: 700; font-size: 13px; color: var(--navy); }
  .tagline__services { font-size: 11.5px; color: var(--slate); margin-top: 4px; }
</style>
</head>
<body>
  <section class="card card--front">
    <div class="name-bar"></div>
    <div class="identity">
      <p class="identity__name">DYLAN MERCER</p>
      <p class="identity__title">President and Coo</p>
    </div>
    <div class="address">
      <p class="address__label">Corporate:</p>
      <p>418 Cedar Avenue, Suite 310</p>
      <p>Port Arden, TX 77790</p>
    </div>
    <ul class="contacts">
      <li><svg viewBox="0 0 12 12"><path d="M3 0h6a1 1 0 0 1 1 1v10a1 1 0 0 1-1 1H3a1 1 0 0 1-1-1V1a1 1 0 0 1 1-1zm0 1.5v8h6v-8z"/></svg>713-555-0142</li>
      <li><svg viewBox="0 0 12 12"><path d="M1 3c0-1 1-2 5-2s5 1 5 2v1H8V3H4v1H1zM2 5h8l1 6H1z"/></svg>877-555-0163</li>
      <li><svg viewBox="0 0 12 12"><path d="M0 2h12v8H0zm1 1v.4l5 3.2 5-3.2V3z"/></svg>Dylan@marrowfieldpartners.com</li>
      <li><svg viewBox="0 0 12 12"><path d="M6 0a6 6 0 1 0 0 12A6 6 0 0 0 6 0zm0 1.2c.9 1 1.4 2.6 1.5 4.2h-3C4.6 3.8 5.1 2.2 6 1.2zM1.3 6.6h2.2c.1 1.5.5 2.9 1.2 3.9a4.8 4.8 0 0 1-3.4-3.9zm7.2 0h2.2a4.8 4.8 0 0 1-3.4 3.9c.7-1 1.1-2.4 1.2-3.9z"/></svg>www.marrowfieldpartners.com</li>
    </ul>
    <div class="brand">
      <span class="brand__dot"></span>
      <span class="brand__name">K&amp;T</span>
    </div>
  </section>

  <section class="card card--back">
    <div class="brand">
      <span class="brand__dot"></span>
      <span class="brand__name">K&amp;T</span>
    </div>
    <div class="divider"></div>
    <div class="anniversary">
      <p class="anniversary__years">20 YEARS</p>
      <p class="anniversary__span">2004-2024</p>
    </div>
    <div class="tagline">
      <p class="tagline__lead">Integrated Industrial Services</p>
      <p class="tagline__services">Mechanical/Civil I&amp;E Fabrication Rotating Heat Transfer Equipment</p>
    </div>
  </section>
</body>
</html>
```